WP website design Fern Ridge (Contest)

We need a wordpress design that will incorporate a professional color scheme with company logo in a clean layout. The design needs to consider that this will be developed on a responsive theme. Colors are blue and green of the logo and and an accent color (perhaps very light brown/tan). Client wants a 'modern' look.

Industry/Entity Type

It Company

Font styles to use
Serif
Sans Serif

Colors

Designer to choose colors to be used in the design.

Requirements
Must have
• Navigation: 1) Home; 2) Upcoming Auctions; 3) Past Auctions; 4) About Us; 5) Services; 6) Sellers; 7) Buyers; 8) Contact Us

Site will have slideshow - image is attached. Colors will be those in the logo, blue and green with maybe an accent color. A site the client mentions liking is talvickbidhall.com for the use of color and layout.

Widgets: 1) Featured Properties; 2) Call to action for Sellers 3) Testimonials blog/widget
Nice to have
• use of dropdown menus

```html
<!DOCTYPE html>
<html lang="en">
<head>
<meta charset="utf-8">
<title>Fern Ridge Auction &amp; Real Estate</title>
<link href="https://fonts.googleapis.com/css2?family=Arimo:wght@400;700&family=PT+Sans:wght@400;700&family=Noto+Sans:wght@400;700&display=swap" rel="stylesheet">
<style>
:root{
  --bg:#e8dcc0;
  --green:#0c6a38;
  --green-dark:#0a5a2f;
  --green-light:#1d7d4b;
  --blue:#0f4a86;
  --blue-dark:#0c3a6a;
  --brown:#5b3218;
  --brown-light:#7a4a2a;
  --cream:#f7e9d8;
  --grey:#e6e6e6;
  --text:#222;
  --red:#c00000;
}
*{box-sizing:border-box;margin:0;padding:0}
html,body{width:1029px;height:1200px;overflow:hidden}
body{background:var(--bg);font-family:"Arimo",Arial,sans-serif;color:var(--text);position:relative}
.page{position:absolute;left:86px;top:0;width:857px;height:1117px;background:#fff}
.masthead{position:absolute;left:0;top:0;width:857px;height:274px;background:#fdfcf3}
.masthead .hero{position:absolute;left:240px;top:0;right:0;height:274px;
  background:linear-gradient(90deg,rgba(253,252,243,1) 0%,rgba(253,252,243,0) 18%),
  linear-gradient(180deg,#8a5a4a 0%,#9b6d5a 35%,#7d9a6a 42%,#a9bfcf 50%,#7e9fb8 60%,#3f8a3a 66%,#2f7d2e 100%)}
.brand{position:absolute;left:17px;top:38px;width:196px;text-align:center;color:var(--green)}
.brand .name{font-weight:700;font-size:27px;line-height:30px;display:flex;align-items:center;gap:6px;justify-content:center}
.brand .dot{width:22px;height:22px;border-radius:50%;background:var(--blue);flex:none}
.brand .rule{height:2px;background:var(--green);margin:34px 4px 14px}
.brand .sub{font-weight:700;font-size:25px;line-height:30px}
.mainnav{position:absolute;left:0;top:274px;width:857px;height:43px;background:var(--green);display:flex}
.mainnav a{display:flex;align-items:center;justify-content:center;color:#fff;text-decoration:none;
  font-family:"PT Sans",sans-serif;font-weight:700;font-size:13.5px;border-right:1px solid #0a5a30}
.mainnav a:last-child{border-right:0}
.mainnav a.active{background:var(--green-light)}
.dropdown{position:absolute;left:463px;top:319px;width:169px;border-bottom:3px solid var(--green)}
.dropdown a{display:block;height:31px;line-height:31px;padding-left:9px;color:#fff;font-family:"Noto Sans",sans-serif;
  font-size:13px;letter-spacing:.5px;text-decoration:none;background:var(--green-light);border:1px solid #0f6a3c}
.dropdown a.hover{background:var(--blue-dark)}
.intro{position:absolute;left:18px;top:348px;width:528px}
.intro h1{font-weight:400;font-size:23px;color:var(--blue);white-space:nowrap;margin-bottom:12px}
.intro p{font-size:12.4px;line-height:19px}
.auction{position:absolute;left:17px;width:554px;height:271px;background:var(--cream);border:1px solid #b9a894;border-radius:5px;overflow:hidden}
.auction header{height:38px;background:linear-gradient(180deg,var(--brown-light),var(--brown));color:#fff;
  font-family:"Noto Sans",sans-serif;font-weight:700;font-size:13.5px;padding:10px 14px;letter-spacing:.3px}
.auction .photo{position:absolute;left:18px;top:57px;width:247px;height:147px;box-shadow:2px 2px 4px rgba(0,0,0,.35);
  background:linear-gradient(180deg,#cfd3d6 0%,#b9bcbc 40%,#6c8b48 60%,#4f7a32 100%)}
.btn{position:absolute;top:225px;width:88px;height:28px;background:var(--green);border-radius:3px;color:#fff;
  font-family:"Noto Sans",sans-serif;font-size:11.5px;display:flex;align-items:center;gap:8px;padding-left:9px;letter-spacing:.4px}
.btn svg{flex:none}
.info{position:absolute;left:291px;top:57px;width:250px;font-family:"Noto Sans",sans-serif;font-size:11px;letter-spacing:.4px;line-height:16.5px}
.info h3{font-size:15.5px;line-height:19px;letter-spacing:.6px;margin-bottom:9px}
.info .sell{font-size:10.5px;line-height:15.5px}
.info .bill{color:var(--red);font-weight:700;font-size:12.5px;text-align:right;margin:5px 0 2px}
.info b{font-weight:700}
.info .addr{display:flex;align-items:center;gap:3px}
.seller-cta{position:absolute;left:615px;top:346px;width:221px;height:61px;border-radius:4px;
  background:linear-gradient(180deg,#1a5ea8,var(--blue-dark));color:#fff}
.seller-cta .play{position:absolute;left:7px;top:10px}
.seller-cta .t1{position:absolute;left:67px;top:4px;font-size:33px}
.seller-cta .t2{position:absolute;left:67px;top:39px;font-size:13px}
.widget{position:absolute;left:603px;width:250px;background:var(--grey);border:1px solid #cfcfcf}
.widget h2{height:36px;font-weight:400;font-size:20px;color:#fff;padding:5px 12px}
.featured h2{background:linear-gradient(180deg,#137a43,var(--green-dark))}
.featured .title{font-weight:700;font-size:13px;text-align:center;margin:19px 8px 16px;line-height:15.5px}
.featured .img{width:154px;height:93px;margin:0 auto;border:2px solid var(--green);
  background:linear-gradient(180deg,#b7c4a8 0%,#8aa07a 45%,#6f8a5a 70%,#4f7a3a 100%)}
.featured .addr{text-align:center;font-size:11px;line-height:14px;margin-top:12px}
.testimonials h2{background:linear-gradient(180deg,#18579a,var(--blue-dark))}
.testimonials .quote{padding:13px 18px 0 18px;font-size:10.5px;line-height:17px}
.testimonials .mark{font-family:Georgia,serif;font-size:24px;line-height:10px;vertical-align:-8px;color:#444}
.testimonials .by{font-size:9.5px;margin-top:10px}
.footer{position:absolute;left:91px;top:1143px;font-size:12px;line-height:15.5px}
.badge{position:absolute;left:768px;top:1134px;width:164px;height:52px;background:#fff;border:1px solid #ccc;border-radius:5px}
.badge span{position:absolute;left:10px;top:12px;width:130px;height:26px;border-radius:13px;background:#c9d6e6}
</style>
</head>
<body>
<div class="page">
  <header class="masthead">
    <div class="hero" role="img" aria-label="Farmland photo: crop field, pond and green soybean rows"></div>
    <div class="brand">
      <div class="name"><span class="dot"></span>Harrow Land Realty</div>
      <div class="rule"></div>
      <div class="sub">Fern Ridge<br>Auction &amp;<br>Real Estate</div>
    </div>
  </header>

  <nav class="mainnav">
    <a style="width:75px">HOME</a>
    <a style="width:167px">UPCOMING AUCTIONS</a>
    <a style="width:135px">PAST AUCTIONS</a>
    <a class="active" style="width:99px">ABOUT US</a>
    <a style="width:96px">SERVICES</a>
    <a style="width:88px">SELLERS</a>
    <a style="width:90px">BUYERS</a>
    <a style="width:107px">CONTACT US</a>
  </nav>

  <section class="intro">
    <h1>Welcome to Harrow Land Real Estate</h1>
    <p>Harrow Land - Fern Ridge Auction Company is the Southeast's premier auction company. Licensed in Georgia and South Carolina, our team has experience selling all types of assets. Whether it is an equestrian property, farm, timberland, or custom home, industrial and farm equipment, a gun or coin collection, classic cars or an estate, Fern Ridge Auction can provide you the marketing resources needed to reach qualified buyers of your particular assets.</p>
  </section>

  <article class="auction" style="top:504px">
    <header>Prairie County Auction-GUNS-COINS-ANTIQUES</header>
    <div class="photo" role="img" aria-label="Photo of a single-storey house with garage and lawn"></div>
    <div class="btn" style="left:44px"><svg width="18" height="16" viewBox="0 0 18 16"><rect x="1" y="3" width="9" height="11" rx="1" fill="#fff"/><rect x="7" y="1" width="10" height="9" rx="2" fill="#dfe8ff"/></svg>Details</div>
    <div class="btn" style="left:158px"><svg width="18" height="16" viewBox="0 0 18 16"><rect x="1" y="2" width="16" height="12" fill="#fff"/><rect x="3" y="6" width="12" height="6" fill="#3a6fc9"/><rect x="3" y="3" width="12" height="2" fill="#c33"/></svg>Photos</div>
    <div class="info">
      <h3>Thursday, August 21st at 10:00 A.M.</h3>
      <p class="sell">Selling 3120 Acres of land in tracts of 2590 Acres&amp; 560 Acres</p>
      <p class="bill">Click here to view Sale Bill!</p>
      <p><b>LIVE OFF-SITE AUCTION</b></p>
      <p><b>Auction Location:</b></p>
      <p class="addr"><svg width="10" height="13" viewBox="0 0 10 13"><path d="M5 12C2 8 1 6 1 4.5a4 4 0 0 1 8 0C9 6 8 8 5 12z" fill="#d00"/><circle cx="5" cy="4.5" r="1.5" fill="#fff"/></svg>418 N Main St, Calder, OK 73950</p>
      <p><b>Property Location:</b></p>
      <p class="addr"><svg width="10" height="13" viewBox="0 0 10 13"><path d="M5 12C2 8 1 6 1 4.5a4 4 0 0 1 8 0C9 6 8 8 5 12z" fill="#d00"/><circle cx="5" cy="4.5" r="1.5" fill="#fff"/></svg>418 N Main St, Calder, OK 73950</p>
      <p><b>Begins:</b>&nbsp;&nbsp;08/21/14 at 10:00 AM CDT</p>
    </div>
  </article>

  <article class="auction" style="top:815px">
    <header>Prairie County Auction-GUNS-COINS-ANTIQUES</header>
    <div class="photo" role="img" aria-label="Photo of a single-storey house with garage and lawn"></div>
    <div class="btn" style="left:44px"><svg width="18" height="16" viewBox="0 0 18 16"><rect x="1" y="3" width="9" height="11" rx="1" fill="#fff"/><rect x="7" y="1" width="10" height="9" rx="2" fill="#dfe8ff"/></svg>Details</div>
    <div class="btn" style="left:158px"><svg width="18" height="16" viewBox="0 0 18 16"><rect x="1" y="2" width="16" height="12" fill="#fff"/><rect x="3" y="6" width="12" height="6" fill="#3a6fc9"/><rect x="3" y="3" width="12" height="2" fill="#c33"/></svg>Photos</div>
    <div class="info">
      <h3>Thursday, August 21st at 10:00 A.M.</h3>
      <p class="sell">Selling 3120 Acres of land in tracts of 2590 Acres&amp; 560 Acres</p>
      <p class="bill">Click here to view Sale Bill!</p>
      <p><b>LIVE OFF-SITE AUCTION</b></p>
      <p><b>Auction Location:</b></p>
      <p class="addr"><svg width="10" height="13" viewBox="0 0 10 13"><path d="M5 12C2 8 1 6 1 4.5a4 4 0 0 1 8 0C9 6 8 8 5 12z" fill="#d00"/><circle cx="5" cy="4.5" r="1.5" fill="#fff"/></svg>418 N Main St, Calder, OK 73950</p>
      <p><b>Property Location:</b></p>
      <p class="addr"><svg width="10" height="13" viewBox="0 0 10 13"><path d="M5 12C2 8 1 6 1 4.5a4 4 0 0 1 8 0C9 6 8 8 5 12z" fill="#d00"/><circle cx="5" cy="4.5" r="1.5" fill="#fff"/></svg>418 N Main St, Calder, OK 73950</p>
      <p><b>Begins:</b>&nbsp;&nbsp;08/21/14 at 10:00 AM CDT</p>
    </div>
  </article>

  <a class="seller-cta">
    <svg class="play" width="48" height="48" viewBox="0 0 48 48"><circle cx="24" cy="24" r="22" fill="#0b2f57" stroke="#5d8fcf" stroke-width="2"/><path d="M19 15l14 9-14 9z" fill="#fff"/></svg>
    <span class="t1">Seller</span>
    <span class="t2">Click Here For Detail</span>
  </a>

  <aside class="widget featured" style="top:436px;height:269px">
    <h2>Featured Property</h2>
    <p class="title">13.35 ACRES OF PRIME DEVELOP &amp; 33RD STREET</p>
    <div class="img" role="img" aria-label="Photo of a white farmhouse with people gathered on the lawn"></div>
    <p class="addr">LOTS 13 &amp; 14 FOR SALE,<br>MARLOW IOWA<br>Third Street, Marlow, IA 52790</p>
  </aside>

  <aside class="widget testimonials" style="top:748px;height:270px">
    <h2>Testimonials Blog</h2>
    <div class="quote">
      <p><span class="mark">&ldquo;</span> Marian I remember you telling me just go back to Atlanta and everything will be taken care of. Anyway I deal with commer cial real estate all over the US and have met some great people , but none top you. It's your presence---</p>
      <p class="by">Brightline Partners</p>
    </div>
  </aside>
</div>

<footer class="footer">
  <p>Copyright © 2014 • Fern Ridge Auction &amp; Real Estate. • All Rights Reserved</p>
  <p>Powered by: BidWorks.net &amp; EMBERLOFT</p>
</footer>
<div class="badge" role="img" aria-label="Partner badge"><span></span></div>

<nav class="dropdown">
  <a>Upcoming auctions</a>
  <a class="hover">Past auctions</a>
</nav>
</body>
</html>
```